We need a redesign of our current website: www.vallowmerehosts.com. Vallowmere Holdings is a fully integrated hospitality development, management, and investment firm. We strive for leadership in each of our segments by building quality assets, exacting high standards of customer service, and focusing on returns for our investors and partners.

It is our mission to provide our guests an exceptional lodging experience; our clients an unsurpassed level of management in their properties; and create positive returns for our investors and partners. We achieve our mission via a company culture of transparency, ownership of our actions, and accountability for our results.

Target Market(s)

hotel owners, hotel developers, hotel investors, bankers

Industry/Entity Type

Hospitality

Requirements
Must have
• Our logo has to be there along with the quote and the ability to convey the following quote off of our current website: "Vallowmere was founded on the principles of integrity, honesty, loyalty, and trust. These convictions embody our company at every level, and show in every action."

```html
<!DOCTYPE html>
<html lang="en">
<head>
<meta charset="utf-8">
<title>Vallowmere Holdings</title>
<link href="https://fonts.googleapis.com/css2?family=Source+Sans+3:wght@400;600&display=swap" rel="stylesheet">
<style>
:root{
  --orange:#d6870f;
  --orange-dark:#b86d05;
  --footer:#d17e06;
  --accent:#e8720c;
  --maroon:#8b1f1f;
  --ink:#222;
  --body:#3a3a3a;
  --panel:#a9c6d6;
  --rule:#dcdcdc;
}
*{margin:0;padding:0;box-sizing:border-box}
html,body{width:1190px;height:1200px;overflow:hidden}
body{position:relative;background:#fff;font-family:"Source Sans 3",Arial,sans-serif;color:var(--body)}
.abs{position:absolute}
.header{left:0;top:0;width:1190px;height:103px;background:linear-gradient(#fff,#eef1f5);border-top:3px solid #222}
.brand{left:145px;top:22px;display:flex;align-items:center;gap:12px}
.brand-dot{width:58px;height:58px;border-radius:50%;background:var(--accent)}
.brand-name{font-size:27px;font-weight:600;color:var(--accent);letter-spacing:2px;line-height:1}
.follow{font-size:13px;color:var(--ink);display:flex;align-items:center;gap:9px}
.follow .sq{width:16px;height:16px;border-radius:3px;background:#7d8fa6}
.header .follow{left:881px;top:41px}
.nav{left:0;top:103px;width:1190px;height:34px;background:linear-gradient(#e39b2b,var(--orange) 50%,var(--orange-dark));border-bottom:1px solid #9c5c04}
.nav a{position:absolute;top:9px;font-size:12px;color:#2a1a05;text-decoration:none;transform:translateX(-50%)}
.nav .sep{position:absolute;top:0;width:1px;height:34px;background:#b06c0c}
.search{left:778px;top:108px;width:233px;height:23px;background:#fff;border:2px solid #e9b56a;font-size:12px;color:#a36a1a;padding:1px 10px}
.hero{left:0;top:139px}
.hero-item{position:absolute;left:161px;width:210px;font-size:11px;line-height:15px;color:#1c1c1c}
.hero-item h3{font-size:12px;font-weight:400;color:var(--maroon);margin-bottom:5px}
.hero-item .more{color:var(--maroon)}
.hero-item::before{content:"";position:absolute;left:-22px;top:4px;border-left:4px solid #222;border-top:3px solid transparent;border-bottom:3px solid transparent}
.sec-icon{width:22px;height:22px;border-radius:50%;background:var(--accent)}
.sec-title{font-size:17px;color:var(--ink);display:flex;align-items:center;gap:12px}
.service{left:138px;width:266px}
.thumb{position:absolute;left:0;top:0;width:90px;height:82px}
.service h4{position:absolute;left:107px;top:-6px;font-size:15px;font-weight:400;color:var(--ink)}
.service p{position:absolute;left:108px;top:17px;width:156px;font-size:12.5px;line-height:15px;text-align:justify;color:#333}
.more{color:var(--accent);font-size:12px}
.dots{left:135px;width:272px;border-top:1px dotted #aaa}
.card{background:#fff;border:1px solid var(--rule);box-shadow:0 6px 14px rgba(0,0,0,.06)}
.card .rule{position:absolute;left:8px;right:8px;border-top:1px solid var(--rule)}
.welcome p{position:absolute;left:18px;top:58px;width:585px;font-size:12px;line-height:21px;text-align:justify;color:#333}
.box p{font-size:12px;line-height:20px;color:#333}
.footer{left:0;top:1061px;width:1190px;height:139px;background:var(--footer);text-align:center;color:#1b1104}
.footer .follow{position:absolute;left:511px;top:37px}
.footer .links{position:absolute;left:0;right:0;top:75px;font-size:11px}
.footer .copy{position:absolute;left:0;right:0;top:97px;font-size:11px}
</style>
</head>
<body>

<header class="abs header">
  <div class="abs brand"><span class="brand-dot"></span><span class="brand-name">VALLOWMERE HOLDINGS</span></div>
  <div class="abs follow">Follow Us <span class="sq"></span><span class="sq"></span><span class="sq"></span><span class="sq"></span></div>
</header>

<nav class="abs nav">
  <a style="left:179px">HOME</a><span class="sep" style="left:240px"></span>
  <a style="left:300px">SERVICES</a><span class="sep" style="left:369px"></span>
  <a style="left:432px">PROJECTS</a><span class="sep" style="left:495px"></span>
  <a style="left:552px">TEAM</a><span class="sep" style="left:618px"></span>
  <a style="left:681px">CONTACT US</a>
</nav>
<div class="abs search">Search
  <svg class="abs" style="right:6px;top:4px" width="12" height="12" viewBox="0 0 12 12"><circle cx="5" cy="5" r="3.5" fill="none" stroke="#e08a10" stroke-width="1.8"/><line x1="7.5" y1="7.5" x2="11" y2="11" stroke="#e08a10" stroke-width="2"/></svg>
</div>

<svg class="abs hero" width="1190" height="430" viewBox="0 0 1190 430">
  <defs>
    <linearGradient id="sideTone" x1="0" x2="0" y1="0" y2="1"><stop offset="0" stop-color="#fff"/><stop offset="1" stop-color="#dfe7ee"/></linearGradient>
    <linearGradient id="photoTone" x1="0" x2="0" y1="0" y2="1"><stop offset="0" stop-color="#3d4248"/><stop offset=".35" stop-color="#6b6156"/><stop offset=".6" stop-color="#a5522f"/><stop offset=".8" stop-color="#3b3a3a"/><stop offset="1" stop-color="#2a2b2b"/></linearGradient>
  </defs>
  <rect x="0" y="30" width="1190" height="385" fill="url(#sideTone)" role="img" aria-label="Soft pale blue floral ornament background"/>
  <rect x="370" y="0" width="706" height="415" fill="url(#photoTone)" role="img" aria-label="Photo of red brick townhouses along a curving road under a stormy sky"/>
  <path d="M115 0 H370 Q405 200 368 415 H115 Z" fill="#a9c6d6"/>
  <g stroke="#c9dbe5" stroke-width="1"><line x1="115" y1="102" x2="389" y2="102"/><line x1="115" y1="198" x2="396" y2="198"/><line x1="115" y1="299" x2="394" y2="299"/></g>
</svg>
<div class="hero-item" style="top:159px"><h3>Meadowline Inn &amp; Suites</h3>Appointed receiver of a 65 room hotel in April 2012.<br><span class="more">read more +</span></div>
<div class="hero-item" style="top:258px"><h3>Harborview Express &amp; Suites</h3>New development opening fall 2012.<br><span class="more" style="line-height:26px">read more +</span></div>
<div class="hero-item" style="top:350px"><h3>Larkfield Suites</h3>Consulting services provided for new development opening in summer 2012.<br><span class="more">read more +</span></div>
<div class="hero-item" style="top:453px"><h3>Wayfarer's Rest Inn</h3>Appointed receiver of a 50-room hotel. Increased cash flow and value; assisted...<br><span class="more">read more +</span></div>

<div class="abs sec-title" style="left:136px;top:603px"><span class="sec-icon"></span>Our Services</div>
<div class="abs" style="left:135px;top:636px;width:250px;border-top:1px solid var(--rule)"></div>

<div class="abs service" style="top:656px">
  <div class="thumb" role="img" aria-label="Aerial site plan illustration of a hotel development" style="background:linear-gradient(135deg,#9cbf7a,#c9a06a 55%,#8fb070)"></div>
  <h4>Development</h4><p>When evaluating sites for purchase and hotel development...<br><span class="more" style="line-height:28px">read more +</span></p>
</div>
<div class="abs dots" style="top:765px"></div>
<div class="abs service" style="top:788px">
  <div class="thumb" role="img" aria-label="Photo of a furnished hotel guest room" style="background:linear-gradient(135deg,#5a4a3a,#c9b79a 55%,#7a6650)"></div>
  <h4>Management</h4><p>Using proven strategies we maximize potential and produce profitable...<br><span class="more" style="line-height:22px">read more +</span></p>
</div>
<div class="abs dots" style="top:899px"></div>
<div class="abs service" style="top:922px">
  <svg class="thumb" viewBox="0 0 90 82" role="img" aria-label="Bar chart of rising hotel value">
    <rect width="90" height="82" fill="#111"/>
    <g fill="#c81818"><rect x="14" y="52" width="7" height="18"/><rect x="28" y="48" width="7" height="22"/><rect x="42" y="44" width="7" height="26"/><rect x="56" y="36" width="7" height="34"/><rect x="70" y="24" width="7" height="46"/></g>
    <line x1="10" y1="70" x2="84" y2="70" stroke="#777"/>
  </svg>
  <h4>Investment</h4><p>Vallowmere recognizes that we are entrusted with investors' capital.<br><span class="more" style="line-height:18px">read more +</span></p>
</div>

<section class="abs card welcome" style="left:447px;top:594px;width:626px;height:198px">
  <div class="abs sec-title" style="left:14px;top:13px"><span class="sec-icon"></span>welcome to our site</div>
  <div class="rule" style="top:47px"></div>
  <p>Vallowmere Holdings is a fully integrated hospitality development, management, and investment firm. We strive for leadership in each of our segments by building quality assets, exacting high standards of customer service, and focusing on returns for our investors and partners. It is our mission to provide our guests an exceptional lodging experience; our clients an unsurpassed level of management in their properties; and create positive returns for our investors and partners. We achieve our mission via a company culture of transparency, ownership of our actions, and accountability for our results.</p>
</section>

<section class="abs card box" style="left:447px;top:822px;width:291px;height:187px;border-color:#fff">
  <div class="abs sec-title" style="left:7px;top:8px"><span class="sec-icon"></span>Team</div>
  <svg class="abs" style="left:253px;top:13px" width="28" height="28" viewBox="0 0 28 28"><g fill="#e8720c"><circle cx="5" cy="4" r="3"/><circle cx="14" cy="4" r="3"/><circle cx="23" cy="4" r="3"/></g><g fill="#111"><rect x="1" y="9" width="26" height="7"/><rect x="2" y="16" width="5" height="12"/><rect x="11" y="16" width="6" height="12"/><rect x="21" y="16" width="5" height="12"/></g></svg>
  <div class="rule" style="top:41px;left:6px;right:6px"></div>
  <p class="abs" style="left:20px;top:67px;width:244px;text-align:justify">As the President and CEO of Vallowmere, Dorin provides the vision and strategic direction for the company. With over 20 years of experience in the hospitality industry...<br><span class="more" style="line-height:34px">read more +</span></p>
</section>

<section class="abs card box" style="left:775px;top:822px;width:281px;height:187px;border-color:#fff">
  <div class="abs sec-title" style="left:2px;top:8px"><span class="sec-icon"></span>Contact us</div>
  <svg class="abs" style="left:256px;top:22px" width="24" height="18" viewBox="0 0 24 18"><rect width="24" height="18" fill="#111"/><path d="M0 0 L12 10 L24 0" fill="none" stroke="#e8720c" stroke-width="3"/><path d="M0 18 L9 9 M24 18 L15 9" stroke="#fff" stroke-width="1"/></svg>
  <div class="rule" style="top:41px;left:0;right:0"></div>
  <p class="abs" style="left:22px;top:58px;line-height:22px">4180 Harlow Ridge Dr. #210<br>Maple Fork, OH 45990<br>Office: 555-318-2047<br>Fax: 555-640-7712<br>info@vallowmereholdings.com</p>
</section>

<footer class="abs footer">
  <div class="follow">Follow Us <span class="sq"></span><span class="sq"></span><span class="sq"></span><span class="sq"></span></div>
  <div class="links">Home &nbsp;| &nbsp;Services &nbsp;| &nbsp;Projects &nbsp;| &nbsp;Team &nbsp;| &nbsp;Contact us</div>
  <div class="copy">Copyrights @ 2012 All Rights Reserved</div>
</footer>

</body>
</html>
```